Desktop and Mobile Site Homepage Redesign

We need a new website homepage redesign for www.plomzar.com. Plomzar is a new startup company based in San Francisco. We develop innovative iPhone application for consumers.
Our initial product is Plomzar that connects tv audiences with their favorite tv shows and fans. We would like to see designs that use the color red. The final design should communicate fun entertainment with social aspects relevant to USA cable tv shows.

We need 1. Desktop website and 2. Mobile website

Target Market(s)

USA

Industry/Entity Type

Entertainment

Number of Pages Required

2 page

Requirements
Must have
• Company name and logo. 1 Page Desktop View and 1 Page Mobile View.
Nice to have
• Details visit www.plomzar.com

```html
<!DOCTYPE html>
<html lang="en">
<head>
<meta charset="utf-8">
<title>Plomzar — Homepage</title>
<link href="https://fonts.googleapis.com/css2?family=Montserrat:wght@400;500;600;700&display=swap" rel="stylesheet">
<style>
:root{
  --red:#ff0000;
  --white:#ffffff;
  --black:#000000;
  --ink:#111111;
  --light:#efefef;
  --mist:#e0e0e0;
  --charcoal:#262626;
  --footer:#222222;
  --steel:#a8a8a8;
  --field:#4a4a4a;
  --phone:#1a1a1a;
}
*{margin:0;padding:0;box-sizing:border-box}
html,body{width:677px;height:1200px;overflow:hidden}
body{position:relative;font-family:'Montserrat',sans-serif;background:var(--white);color:var(--ink)}
.block{position:absolute;left:0;width:677px}
.site-header{top:0;height:41px;background:var(--white)}
.brand{position:absolute;left:11px;top:7px;display:flex;align-items:center;gap:5px;color:var(--red);font-size:21px;font-weight:500;line-height:26px}
.brand-dot{width:12px;height:12px;border-radius:50%;background:var(--red)}
.signup{position:absolute;left:592px;top:10px;width:68px;height:20px;border:2px solid var(--red);color:var(--red);font-size:7px;font-weight:700;letter-spacing:1.2px;display:flex;align-items:center;justify-content:center}
.hero{top:41px;height:313px;background:var(--black);color:var(--white);text-align:center}
.hero h1{position:absolute;left:0;right:0;top:95px;font-size:30px;font-weight:700;line-height:34px}
.hero p{position:absolute;left:0;right:0;top:177px;font-size:11px;font-weight:600}
.cta{position:absolute;left:283px;top:213px;width:107px;height:29px;background:var(--red);font-size:7px;font-weight:700;letter-spacing:1.3px;display:flex;align-items:center;justify-content:center}
.arrow{position:absolute;top:145px}
.arrow.prev{left:20px}.arrow.next{left:640px}
.dots{position:absolute;left:324px;top:293px;display:flex;gap:3px}
.dots span{width:4px;height:4px;border-radius:50%;background:var(--white)}
.intro{top:354px;height:164px;background:var(--light);text-align:center}
.intro h2{position:absolute;left:0;right:0;top:42px;color:var(--red);font-size:21px;font-weight:700}
.intro p{position:absolute;left:120px;right:120px;top:82px;font-size:11px;line-height:16px}
.feature h2{position:absolute;color:var(--red);font-size:20px;font-weight:700}
.feature p{position:absolute;width:290px;font-size:11px;line-height:16px}
.sports{top:518px;height:206px;background:var(--charcoal);color:var(--white)}
.sports h2{left:46px;top:53px}
.sports p{left:45px;top:98px}
.reality{top:724px;height:201px;background:var(--mist)}
.reality h2{right:63px;top:41px}
.reality p{right:61px;top:86px;text-align:right}
.device{position:absolute;background:var(--phone);border:2px solid #555;border-bottom:none;border-radius:22px 22px 0 0}
.device .speaker{position:absolute;top:18px;left:50%;margin-left:-12px;width:24px;height:2px;background:#555;border-radius:1px}
.device .cam{position:absolute;top:17px;left:50px;width:4px;height:4px;border-radius:50%;background:#444}
.screen{position:absolute;left:9px;right:9px;bottom:0}
.sports .device{left:463px;top:24px;width:152px;height:182px}
.sports .screen{top:34px;background:linear-gradient(160deg,#c9d3e2 0%,#2f4fa8 45%,#1c2f78 100%)}
.reality .device{left:54px;top:26px;width:152px;height:175px}
.reality .screen{top:36px;background:linear-gradient(180deg,#5a4fa0 0%,#d9d9d9 35%,#f4f4f0 65%,#1b2d78 100%)}
.share{top:925px;height:133px;width:338px;background:var(--charcoal);color:var(--white);text-align:center}
.share h3{position:absolute;left:0;right:0;top:35px;font-size:21px;font-weight:600}
.share p{position:absolute;left:0;right:0;top:60px;font-size:10px}
.social{position:absolute;left:0;right:0;top:93px;display:flex;justify-content:center;gap:18px;align-items:center}
.social span{width:13px;height:13px;border-radius:50%;background:var(--white)}
.chat{top:925px;left:338px;width:339px;height:133px;background:var(--steel);text-align:center}
.chat svg{position:absolute;left:153px;top:34px}
.chat h3{position:absolute;left:0;right:0;top:75px;color:var(--red);font-size:17px;font-weight:700}
.chat p{position:absolute;left:0;right:0;top:98px;font-size:8px;font-weight:500}
.site-footer{top:1058px;height:142px;background:var(--footer);color:var(--white)}
.footer-nav{position:absolute;left:32px;top:47px;display:flex;gap:11px;font-size:13px;font-weight:600}
.footer-info{position:absolute;left:30px;top:81px;font-size:8.5px;font-weight:600;line-height:11px}
.footer-info span{margin-right:10px}
.newsletter h4{position:absolute;left:434px;top:23px;font-size:13px;font-weight:600}
.email-field{position:absolute;left:432px;top:49px;width:202px;height:23px;background:var(--field)}
.subscribe{position:absolute;left:432px;top:82px;width:74px;height:22px;background:var(--white);color:var(--red);font-size:6px;font-weight:700;display:flex;align-items:center;justify-content:center}
</style>
</head>
<body>
<header class="block site-header">
  <div class="brand"><span class="brand-dot"></span>Plomzar</div>
  <div class="signup">SIGN UP</div>
</header>

<section class="block hero">
  <h1>Plomzar is a new startup company<br>based in San Francisco.</h1>
  <p>Plomzar connects TV audiences with their favourite TV shows and fans.</p>
  <div class="cta">FIND OUT MORE</div>
  <svg class="arrow prev" width="16" height="22" viewBox="0 0 16 22"><polyline points="12,2 3,11 12,20" fill="none" stroke="#fff" stroke-width="2"/></svg>
  <svg class="arrow next" width="16" height="22" viewBox="0 0 16 22"><polyline points="4,2 13,11 4,20" fill="none" stroke="#fff" stroke-width="2"/></svg>
  <div class="dots"><span></span><span></span><span></span><span></span></div>
</section>

<section class="block intro">
  <h2>Turn On our TV and Join The Fans In Real Time</h2>
  <p>Stay connected to other fans who are watching your favourite shows and invite people you know to a private group chat.</p>
</section>

<section class="block feature sports">
  <h2>Live Sports Chatrooms</h2>
  <p>Stay connected to other fans who are watching your favourite Live sports shows and invite people you know to a private group chat.</p>
  <div class="device"><span class="cam"></span><span class="speaker"></span>
    <div class="screen" role="img" aria-label="Photo of a football player in a blue uniform holding a ball"></div>
  </div>
</section>

<section class="block feature reality">
  <div class="device"><span class="cam"></span><span class="speaker"></span>
    <div class="screen" role="img" aria-label="Blurred photo of a brightly lit reality TV stage"></div>
  </div>
  <h2>Reality TV Chatrooms</h2>
  <p>Stay connected to other fans who are watching your favourite Live sports shows and invite people you know to a private group chat.</p>
</section>

<section class="block share">
  <h3>Share and Invite</h3>
  <p>Your Friends To Any TV Show</p>
  <div class="social">
    <span></span><span></span>
    <svg width="16" height="12" viewBox="0 0 16 12"><rect x="0.5" y="0.5" width="15" height="11" fill="none" stroke="#fff"/><polyline points="0.5,0.5 8,7 15.5,0.5" fill="none" stroke="#fff"/></svg>
    <span></span>
  </div>
</section>

<section class="block chat">
  <svg width="30" height="28" viewBox="0 0 30 28"><ellipse cx="15" cy="12" rx="13" ry="11.5" fill="#ff0000"/><polygon points="6,19 3,27 13,22" fill="#ff0000"/></svg>
  <h3>Live Chat With Real Fans</h3>
  <p>See What Your Friends Are Watching On TV</p>
</section>

<footer class="block site-footer">
  <nav class="footer-nav"><span>About Us</span><span>Blog</span><span>Contact Us</span></nav>
  <div class="footer-info"><span>Info@plomzar.com</span>1180 Harbor Lane, Pinecrest, CA 94012<br>Copyright 2017 Plomzar, Inc.</div>
  <div class="newsletter">
    <h4>Get The Latest Update</h4>
    <div class="email-field"></div>
    <div class="subscribe">SUBSCRIBE NOW</div>
  </div>
</footer>
</body>
</html>
```